Design a Flyer for Real Estate Agent

We require a flyer for a real estate agents that sells Luxury Homes on the Sunshine Coast in Australia. The flyer will be letter box dropped and sent to prospective sellers so it must be targeted towards people wanting to sell their homes.
The flyer will contain a bio of the agent and some testimonials etc. The company logo is black and yellow (see attached) and the flyer will need to appeal to the high end of the real estate market.
Flyer can be an open a4, a folded A4 or a traditional flyer, no rules just want something that is eye catching and modern and crisp.
Any questions please ask.
Contact Details to be added to the flyer:
Marcus Dunthorpe
Elite Sales Specialist
m: 0452 906 283
e: marcus@brellowrealty.example
o: 07 5836 2700

```html
<!DOCTYPE html>
<html lang="en">
<head>
<meta charset="utf-8">
<title>Marcus Dunthorpe – Elite Sales Specialist</title>
<link href="https://fonts.googleapis.com/css2?family=Open+Sans:wght@400;600&display=swap" rel="stylesheet">
<style>
  :root {
    --ink: #0d0d0d;
    --panel: #141414;
    --gold: #f5c400;
    --gold-soft: #ffd83a;
    --paper: #ffffff;
    --stage: #ececec;
    --text-light: #f2f2f2;
  }
  * { box-sizing: border-box; margin: 0; padding: 0; }
  html, body { width: 1200px; height: 944px; overflow: hidden; }
  body {
    background: var(--stage);
    font-family: "Open Sans", sans-serif;
    color: var(--text-light);
  }
  .spread {
    position: absolute; top: 72px; left: 190px;
    display: flex; gap: 60px;
  }
  .flyer {
    position: relative; width: 380px; height: 800px;
    background: var(--panel); overflow: hidden;
  }
  .flyer-art { position: absolute; inset: 0; }
  .hero-photo {
    position: absolute; left: 0; top: 0; width: 380px; height: 260px;
    background: linear-gradient(180deg, #5a7fb0 0%, #9db4cf 35%, #a77a55 65%, #5b3d27 100%);
  }
  .agent-portrait {
    position: absolute; left: 34px; top: 222px; width: 124px; height: 132px;
    background: var(--paper); padding: 5px;
  }
  .agent-portrait span {
    display: block; width: 100%; height: 100%;
    background: linear-gradient(180deg, #d9d9d9 0%, #9a9a9a 60%, #3a3a3a 100%);
  }
  .brand {
    position: absolute; display: flex; align-items: center; gap: 8px;
    font-size: 22px; font-weight: 400; color: var(--paper);
  }
  .brand-dot { width: 18px; height: 18px; border-radius: 50%; background: var(--gold); }
  .front .brand { left: 176px; top: 268px; }
  .agent-id { position: absolute; right: 28px; top: 352px; text-align: right; }
  .agent-name { font-size: 27px; font-weight: 400; line-height: 1.1; color: var(--paper); }
  .agent-role { font-size: 12.5px; letter-spacing: .5px; text-transform: uppercase; margin-top: 2px; }
  .body-copy {
    position: absolute; left: 26px; right: 26px;
    font-size: 13px; line-height: 1.58; text-align: justify; hyphens: auto;
  }
  .front .body-copy { top: 420px; }
  .back .body-copy { top: 92px; font-size: 12.6px; }
  .back .body-copy p + p { margin-top: 8px; }
  .back .brand { left: 26px; top: 600px; }
  .contact {
    position: absolute; left: 26px; top: 652px;
    color: var(--gold); font-size: 14px; line-height: 1.5; list-style: none;
  }
</style>
</head>
<body>
<main class="spread">

  <article class="flyer front">
    <div class="hero-photo" role="img" aria-label="Photograph of a luxury Mediterranean-style home at dusk"></div>
    <svg class="flyer-art" viewBox="0 0 380 800" aria-hidden="true">
      <path d="M0,252 C110,254 190,214 255,216 C315,218 350,200 380,188 L380,800 L0,800 Z" fill="var(--panel)"/>
      <path d="M255,216 C315,218 350,200 380,188" fill="none" stroke="var(--gold)" stroke-width="4"/>
      <path d="M0,784 L380,758 L380,772 L0,798 Z" fill="var(--gold)"/>
    </svg>
    <div class="agent-portrait"><span role="img" aria-label="Portrait photo of the agent"></span></div>
    <div class="brand"><span>Brellow</span><span class="brand-dot"></span></div>
    <header class="agent-id">
      <h1 class="agent-name">Marcus Dunthorpe</h1>
      <p class="agent-role">Elite Sales Specialist</p>
    </header>
    <p class="body-copy">If you're looking for a proven track record across all aspects of real estate, then look no further than Marcus Dunthorpe. Entering the industry in 1998, Marcus has years of experience in real estate sales and property finance. Marcus truly understands what it takes to be successful in the competitive world of real estate and has been involved in hundreds of millions of dollars in property sales and settlements. Marcus offers not only world class service to all his clients but is committed to making sure they receive up to date and educated advice at all times during the selling process. This commitment married with first class sales and marketing strategies ensures the best possible outcome is always achieved.</p>
  </article>

  <article class="flyer back">
    <svg class="flyer-art" viewBox="0 0 380 800" aria-hidden="true">
      <path d="M0,0 L380,0 L380,58 C300,40 210,62 130,52 C70,45 25,58 0,70 Z" fill="var(--gold)"/>
      <path d="M0,0 L200,0 L200,57 C150,58 120,50 80,48 C45,47 20,58 0,70 Z" fill="var(--gold-soft)"/>
      <path d="M0,772 L380,756 L380,800 L0,800 Z" fill="var(--gold)"/>
    </svg>
    <div class="body-copy">
      <p>Marcus believes that one of the most important aspects of being successful in real estate is constant, transparent and honest communication between all parties; if everyone is on the same page with the same goal in mind then success is assured.</p>
      <p>With offices across Brisbane, Sunshine Coast and the Gold Coast which incorporate teams of Finance Specialists and Financial Planners as well as a Training Centre, Brellow is changing the way people buy, sell and finance property by being the first and best wholly owned 'end-to-end' property based business. This will be done by truly 'caring' for our clients needs.</p>
      <p>In any property transaction a chain of events is triggered which are not currently serviced by the industry. Brellow is providing solutions for taking people from their initial real estate dream to meeting their eventual goal of financial security.</p>
      <p>The Brellow group works closely as a complete team to provide clients with comprehensive service to Property Sales and Rentals, Finance, Financial Planning, an RTO and more.</p>
    </div>
    <div class="brand"><span>Brellow</span><span class="brand-dot"></span></div>
    <ul class="contact">
      <li>m: 0452 906 283</li>
      <li>o: 07 5836 2700</li>
      <li>e: marcus@brellowrealty.example</li>
      <li>www.brellowrealty.example</li>
    </ul>
  </article>

</main>
</body>
</html>
```